グローバルナビ
左サイドメニュー
横幅:960px

今回は、コンペ用のデザイン作成依頼となります。ロゴや電話番号・その他画像データ等サンプルで作成頂ければ幸いです。

《クライアント様からの要望》
すっきりとした見やすいホームページで、患者様やご家族の方に優しい・温かいイメージをもって欲しい。
ロゴに使用されているカラーコードは、「24569d」となります。基調色として取り入れてください。

総合病院で診療科目が多い為、利用者が情報を探しやすいように工夫してください。
病院のPRポイントとしては、「救急患者の受入れを断らない」地域に最先端医療で貢献する。等

(topページに必要なコンテンツ)
・病院からのお知らせ
・はじめてご来院の方へ
-外来受診のご案内
-診療担当・日時
-休診・代診のお知らせ
-入院のご案内
-セカンドオピニオンについて
・お見舞いの皆様へ
・診療科・施設のご案内
-※別途、診療科・施設については添付ファイルを参照ください。
・当院の紹介
・採用情報
・先進医療センター
・周産期医療センター
・消化器病センター
・乳腺診療センター
・地域医療連携への取り組み
ブルーを基調(ロゴカラーコード:24569d)差し色はお任せ
デザインの作成は、Photoshop・Fireworksのみとなります。Illustratorでの作成は不可とします。
(デザイン参考URL)
http://www.tomaru-kenseikai.gr.jp/
http://www.hanamizuki-kai.or.jp/
http://kobe.nskmu.ac.jp/

現サイトのURLにつきましては、個別にメッセージにてお送りさせて頂きますので、希望される方はメッセージをお送りください。
診療科・その他施設一覧ファイルを追加しました。
既存サイトのURLをお伝えした場合、既存サイトのデザインと同じようなご提案が多いため、期間を延長させて頂きます。
既存サイトのURLはお伝えしませんので、斬新なデザインのご提案をお待ちしております。

全体的にスッキリとしている。病院側の伝えたいポイントをしっかりと捉えている。見やすい等、選定理由となりました。

今回、デザイン作成に応募いただきましてありがとうございます。ご提案いただきました全てのデザインをクライアント様に確認いただき、選定させていただきました。
今後とも、機会がありましたら宜しくお願いいたします。

```html
<!DOCTYPE html>
<html lang="ja">
<head>
<meta charset="utf-8">
<title>若葉総合病院</title>
<link href="https://fonts.googleapis.com/css2?family=Noto+Sans+JP:wght@400;500;700&family=Noto+Serif+JP:wght@500;700&display=swap" rel="stylesheet">
<style>
:root{
  --brand:#24569d;
  --brand-dark:#1a4280;
  --line:#c9d5e6;
  --text:#333;
  --muted:#777;
  --accent:#e0506a;
  --internal:#e06a86;
  --surgery:#ef9a3a;
  --radiology:#6db35a;
  --bg-soft:#f4f7fb;
}
*{box-sizing:border-box;margin:0;padding:0}
html,body{width:1200px;height:2500px;overflow:hidden}
body{font-family:"Noto Sans JP",sans-serif;color:var(--text);background:#fff;font-size:15px;line-height:1.5;position:relative}
a{color:inherit;text-decoration:none}
ul{list-style:none}

/* header */
.site-header{height:140px;position:relative;border-top:4px solid var(--brand)}
.brand{position:absolute;left:24px;top:30px;display:flex;align-items:center;gap:16px}
.brand-dot{width:64px;height:64px;border-radius:50%;background:var(--brand)}
.brand-name{font-family:"Noto Serif JP",serif;font-weight:700;font-size:38px;color:var(--brand);line-height:1.1;letter-spacing:.08em}
.brand-sub{font-family:"Noto Serif JP",serif;font-weight:700;font-size:14px;color:var(--brand);letter-spacing:.16em;display:block;margin-top:4px}
.util-nav{position:absolute;right:16px;top:0;display:flex;gap:4px}
.util-nav a{background:var(--brand);color:#fff;font-size:13px;padding:4px 16px;border-radius:0 0 4px 4px}
.font-size{position:absolute;right:16px;top:40px;font-size:13px;color:var(--muted);display:flex;gap:4px;align-items:center}
.font-size .btn{border:1px solid var(--line);padding:0 8px;color:var(--text);background:#fff}
.tel{position:absolute;right:16px;top:58px;font-size:36px;line-height:1.2;color:var(--accent);font-weight:500;letter-spacing:.04em;white-space:nowrap}
.search{position:absolute;right:16px;top:108px;display:flex;gap:6px;align-items:center}
.search .field{width:220px;height:24px;border:1px solid var(--line)}
.search .go{background:var(--accent);color:#fff;font-size:12px;padding:3px 14px;border-radius:3px}

/* hero */
.hero{position:relative;height:560px}
.hero-photo{position:absolute;inset:0;background:linear-gradient(180deg,#a9c9ea 0%,#d7e7f5 50%,#b7c7b0 78%,#8fa58a 100%)}
.hero-copy{position:absolute;left:40px;top:60px;font-family:"Noto Serif JP",serif;font-weight:700;font-size:40px;line-height:1.6;color:#fff;text-shadow:0 0 8px rgba(20,60,120,.8)}

/* columns */
.main{display:grid;grid-template-columns:260px 660px 240px;gap:20px;padding:30px 0 0 0}

/* left */
.side-nav{border-top:2px solid var(--brand)}
.side-nav li a{display:flex;align-items:center;gap:10px;height:54px;padding-left:16px;border-bottom:1px solid var(--line);font-size:15px}
.side-nav li a::before{content:"";width:0;height:0;border-left:7px solid var(--brand);border-top:5px solid transparent;border-bottom:5px solid transparent}
.side-nav li.current a{background:var(--brand);color:#fff}
.side-nav li.current a::before{border-left-color:#fff}
.contact{margin-top:60px}
.contact h2{font-size:17px;color:var(--brand);border-bottom:2px solid var(--brand);padding:0 0 4px 8px}
.contact .hours{font-size:12px;color:var(--muted);margin:6px 0 10px 8px}
.contact li{padding:14px 0 14px 14px;border-bottom:1px dotted var(--line)}
.contact .name{font-size:14px;color:var(--brand);font-weight:700;display:flex;align-items:center;gap:6px}
.contact .name::before{content:"";width:8px;height:8px;background:var(--brand)}
.contact .num{font-size:14px;padding-left:14px;display:block}

/* center */
.section-title{display:flex;align-items:center;gap:8px;font-size:18px;color:var(--brand);font-weight:700;border-bottom:2px solid var(--brand);padding-bottom:6px;margin-bottom:14px}
.section-title::before{content:"";width:14px;height:14px;background:var(--brand);border-radius:2px}
.section-title .more{margin-left:auto;font-size:13px;font-weight:400;color:var(--text)}
.departments{display:grid;grid-template-columns:repeat(3,1fr);gap:14px;height:520px}
.dept{border:1px solid var(--line);background:var(--bg-soft)}
.dept h3{color:#fff;font-size:16px;padding:8px 14px}
.dept.internal h3{background:var(--internal)}
.dept.surgery h3{background:var(--surgery)}
.dept.radiology h3{background:var(--radiology)}
.dept ul{padding:10px 14px}
.dept li{font-size:14px;padding:7px 0 7px 14px;border-bottom:1px dotted var(--line);position:relative}
.dept li::before{content:"›";position:absolute;left:2px;color:var(--brand)}
.news{margin-top:50px}
.news li{display:flex;align-items:center;gap:16px;padding:13px 4px;border-bottom:1px dotted var(--line);font-size:14px}
.news time{color:var(--muted);width:90px}
.tag{font-size:12px;color:#fff;padding:2px 0;width:80px;text-align:center}
.tag.partner{background:var(--internal)}
.tag.info{background:var(--brand)}
.news .title{color:var(--brand)}
.facilities{margin-top:50px}
.facility-list{display:grid;grid-template-columns:1fr 1fr;column-gap:30px}
.facility-list li{font-size:14px;padding:11px 0 11px 18px;border-bottom:1px dotted var(--line);position:relative}
.facility-list li::before{content:"";position:absolute;left:4px;top:18px;border-left:6px solid var(--brand);border-top:4px solid transparent;border-bottom:4px solid transparent}

/* right */
.guide{border:1px solid var(--line)}
.guide h2{background:var(--brand);color:#fff;font-size:18px;text-align:center;padding:12px 0}
.guide dl{padding:6px 18px 16px}
.guide dt{font-size:14px;font-weight:700;color:var(--brand);margin-top:16px;border-bottom:1px solid var(--line)}
.guide dd{font-size:14px;padding:4px 0 0 16px}
.recruit{display:block;margin-top:28px;height:140px;position:relative;border:1px solid var(--line)}
.recruit-photo{position:absolute;right:0;top:0;width:100px;height:100%;background:linear-gradient(180deg,#dfe8f2,#b8cadf)}
.recruit p{position:absolute;left:14px;top:30px;font-size:17px;font-weight:700;color:var(--brand);line-height:1.5}
.banners{margin-top:28px;display:flex;flex-direction:column;gap:14px}
.banner{height:72px;border:1px solid var(--line);display:flex;align-items:center;justify-content:center;font-size:15px;font-weight:700;color:var(--brand);background:var(--bg-soft)}
.banner.green{background:#6aa84f;color:#fff;border:none}
.banner.blue{background:var(--brand);color:#fff;border:none}
.banner.badge{justify-content:flex-start;gap:12px;padding-left:16px}
.banner.badge .seal{width:48px;height:48px;border-radius:50%;background:#7bb36a}

/* footer */
.pagetop{position:absolute;left:0;top:2070px;width:1200px;text-align:right;padding-right:16px;font-size:13px;color:var(--brand)}
.site-footer{position:absolute;left:0;top:2110px;width:1200px;border-top:3px solid var(--brand);background:var(--bg-soft);height:170px}
.site-footer address{font-style:normal;position:absolute;left:24px;top:28px;font-size:14px;line-height:1.9}
.site-footer small{position:absolute;right:20px;bottom:26px;font-size:12px;color:var(--brand)}
</style>
</head>
<body>
<header class="site-header">
  <a class="brand" href="#"><span class="brand-dot"></span><span class="brand-name">若葉総合病院<span class="brand-sub">Wakaba General Hospital</span></span></a>
  <nav class="util-nav"><a href="#">お問い合わせ</a><a href="#">サイトマップ</a><a href="#">English</a></nav>
  <div class="font-size">文字の大きさ <span class="btn">標準</span><span class="btn">大</span></div>
  <div class="tel">03-4521-8760</div>
  <div class="search"><span class="field"></span><a class="go" href="#">サイト内検索</a></div>
</header>

<section class="hero">
  <div class="hero-photo" role="img" aria-label="青空の下に建つ病院の建物群の写真"></div>
  <p class="hero-copy">救急患者の受入れを断らない<br>地域に最先端医療で貢献する</p>
</section>

<div class="main">
  <aside>
    <ul class="side-nav">
      <li class="current"><a href="#">HOME</a></li>
      <li><a href="#">はじめてご来院の方へ</a></li>
      <li><a href="#">お見舞いの皆様へ</a></li>
      <li><a href="#">当院のご紹介</a></li>
      <li><a href="#">交通アクセス</a></li>
    </ul>
    <div class="contact">
      <h2>各施設へのお問い合わせ</h2>
      <p class="hours">受付時間 8:00～17:00（土日祝を除く）</p>
      <ul>
        <li><span class="name">第一病院</span><span class="num">TEL. 0120-88-4410</span></li>
        <li><span class="name">第二病院</span><span class="num">TEL. 0120-88-4420</span></li>
        <li><span class="name">第三病院</span><span class="num">TEL. 0120-88-4430</span></li>
        <li><span class="name">第四病院</span><span class="num">TEL. 0120-88-4440</span></li>
        <li><span class="name">第五病院</span><span class="num">TEL. 0120-88-4450</span></li>
      </ul>
    </div>
  </aside>

  <main>
    <section>
      <h2 class="section-title">診療科のご案内</h2>
      <div class="departments">
        <div class="dept internal"><h3>内科</h3><ul>
          <li>総合内科・消化器内科</li><li>神経内科</li><li>呼吸器内科</li><li>循環器内科</li><li>腎臓内科</li><li>糖尿病内科</li><li>小児科</li><li>精神科</li><li>救急診療科</li></ul></div>
        <div class="dept surgery"><h3>外科</h3><ul>
          <li>一般外科</li><li>乳腺外科</li><li>消化器外科</li><li>心臓血管外科</li><li>整形外科</li><li>脳神経外科</li><li>泌尿器科</li><li>皮膚科</li><li>眼科</li><li>歯科口腔外科</li><li>産科</li><li>婦人科</li></ul></div>
        <div class="dept radiology"><h3>放射線科</h3><ul>
          <li>放射線診断科</li><li>リハビリテーション科</li><li>麻酔科</li><li>病理診断科</li></ul></div>
      </div>
    </section>

    <section class="news">
      <h2 class="section-title">お知らせ<a class="more" href="#">一覧</a></h2>
      <ul>
        <li><time>2012/10/16</time><span class="tag partner">医療連携</span><span class="title">医療連携室のページを更新しました</span></li>
        <li><time>2012/10/12</time><span class="tag info">お知らせ</span><span class="title">外来診療担当医表を更新しました</span></li>
        <li><time>2012/10/04</time><span class="tag info">お知らせ</span><span class="title">季節性インフルエンザについて</span></li>
        <li><time>2012/09/28</time><span class="tag partner">医療連携</span><span class="title">医療連携室の案内ページを更新しました</span></li>
        <li><time>2012/09/20</time><span class="tag info">お知らせ</span><span class="title">休診・代診のお知らせを更新しました</span></li>
      </ul>
    </section>

    <section class="facilities">
      <h2 class="section-title">施設のご案内</h2>
      <ul class="facility-list">
        <li>総合リハビリテーションセンター</li><li>消化器病センター</li>
        <li>通所リハビリテーションセンター</li><li>周産期医療センター</li>
        <li>在宅医療センター</li><li>乳腺診療センター</li>
        <li>健診センター</li><li>透析室</li>
        <li>手術棟</li><li>薬局</li>
        <li>栄養管理室</li><li>臨床検査センター</li>
        <li>地域リハビリテーション広域支援センター</li><li>MRI室</li>
      </ul>
    </section>
  </main>

  <aside>
    <section class="guide">
      <h2>診療のご案内</h2>
      <dl>
        <dt>診察時間</dt><dd>8:00 ～ 12:00<br>13:00 ～ 16:00</dd>
        <dt>受付時間</dt><dd>8:00 ～ 11:30<br>13:00 ～ 15:30</dd>
        <dt>救急外来</dt><dd>24時間受付</dd>
        <dt>休診日</dt><dd>土曜・日曜・祝日</dd>
        <dt>面会時間</dt><dd>午後2時～午後8時</dd>
      </dl>
    </section>
    <a class="recruit" href="#">
      <div class="recruit-photo" role="img" aria-label="医療スタッフの写真"></div>
      <p>医師・看護師<br>その他スタッフ<br>募集中</p>
    </a>
    <div class="banners">
      <a class="banner" href="#">先進医療センター</a>
      <a class="banner green" href="#">治験審査委員会</a>
      <a class="banner" href="#">管理栄養士のキッチン講座</a>
      <a class="banner blue" href="#">地域医療連携室</a>
      <a class="banner" href="#">健康だより</a>
      <a class="banner badge" href="#"><span class="seal"></span>病院機能評価</a>
    </div>
  </aside>
</div>

<div class="pagetop">▲ ページの先頭へ</div>
<footer class="site-footer">
  <address>〒105-0099<br>東京都港区芝浦9丁目8-7<br>TEL：03-4521-8760</address>
  <small>Copyright © Wakaba General Hospital All rights reserved.</small>
</footer>
</body>
</html>
```